Postcard Design

I am a mortgage broker located in Michigan. I recently opened my own company after working for another for 7 years. I want to send out a mailing letting my old clients know my new information and also reach out to them to let me know if I can assist them with anything.

Industry/Entity Type

It Company

```html
<!DOCTYPE html>
<html lang="en">
<head>
<meta charset="utf-8">
<title>Northgate Mortgage – Postcard</title>
<link href="https://fonts.googleapis.com/css2?family=Roboto+Condensed:wght@400;700&family=Anton&family=Tinos&display=swap" rel="stylesheet">
<style>
  :root {
    --navy: #232a66;
    --navy-deep: #1a1f52;
    --red: #d9261f;
    --red-dark: #8f1410;
    --brand-blue: #2b6cb8;
    --sky: #7fa9dc;
    --facade: #c9a27e;
    --yellow: #ffe11a;
    --orange: #f39a1d;
    --phone-blue: #7cc6f5;
    --phone-red: #d9261f;
    --paper: #ffffff;
    --panel-grey: #ededed;
    --ink: #2a2a2a;
    --stage: #e6e3df;
  }
  * { box-sizing: border-box; margin: 0; padding: 0; }
  html, body { width: 1200px; height: 1000px; overflow: hidden; background: var(--stage); }
  body { position: relative; font-family: "Roboto Condensed", Arial, sans-serif; }

  .card { position: absolute; box-shadow: 0 6px 16px rgba(0,0,0,.35); overflow: hidden; }

  /* Front */
  .card-front { left: 36px; top: 30px; width: 596px; height: 460px; background: var(--navy); }
  .front-photo { position: absolute; left: 0; top: 0; width: 596px; height: 362px;
    background: linear-gradient(180deg, var(--sky) 0%, #cfe0f2 38%, var(--facade) 62%, #b99a7a 82%, #6f8a4a 100%); }
  .front-bands { position: absolute; left: 0; top: 0; }
  .web-pill { position: absolute; display: flex; align-items: center; justify-content: center;
    background: linear-gradient(180deg, #fff25a, var(--yellow) 60%, #f0c400);
    border-radius: 4px; color: #1a1a1a; font-weight: 700; box-shadow: 0 2px 3px rgba(0,0,0,.35); white-space: nowrap; }
  .card-front .web-pill { left: 32px; top: 43px; width: 262px; height: 24px; font-size: 15px; }
  .cursor { position: absolute; }
  .card-front .cursor { left: 289px; top: 56px; }
  .brand-name { position: absolute; font-family: "Roboto Condensed", Arial, sans-serif;
    font-weight: 700; color: var(--brand-blue); letter-spacing: .3px; white-space: nowrap; }
  .card-front .brand-name { left: 336px; top: 114px; font-size: 22px; }
  .brand-mark { display: inline-block; width: 14px; height: 14px; border-radius: 50%;
    background: var(--brand-blue); margin-right: 7px; vertical-align: 1px; }
  .portrait-frame { position: absolute; left: 43px; top: 128px; width: 194px; height: 255px;
    background: #fff; padding: 8px; box-shadow: 0 3px 8px rgba(0,0,0,.4); }
  .portrait { width: 100%; height: 100%; background: linear-gradient(180deg, #6b6b68, #3f3f3f 60%, #2b3040); }
  .agent-name { position: absolute; left: 50px; top: 388px; color: #fff;
    font-family: "Tinos", "Times New Roman", serif; font-size: 21px; white-space: nowrap; }
  .agent-name small { font-size: 12px; margin-left: 6px; }
  .phone { display: flex; align-items: center; font-weight: 700; white-space: nowrap; }
  .card-front .phone { position: absolute; left: 50px; top: 414px; color: var(--phone-blue); font-size: 27px; }
  .phone svg { margin-right: 6px; }
  .welcome { position: absolute; left: 288px; top: 372px; font-family: "Anton", Impact, sans-serif;
    font-size: 48px; line-height: 1.05; letter-spacing: 2.5px;
    background: linear-gradient(180deg, var(--yellow) 35%, var(--orange) 85%);
    -webkit-background-clip: text; background-clip: text; color: transparent; }
  .welcome-sub { position: absolute; left: 289px; top: 421px; color: #fff; font-weight: 700; font-size: 17px; letter-spacing: .2px; white-space: nowrap; }

  /* Back */
  .card-back { left: 570px; top: 512px; width: 596px; height: 460px; background: var(--paper); }
  .back-shapes { position: absolute; left: 0; top: 0; }
  .card-back .brand-name { left: 24px; top: 102px; font-size: 18px; }
  .return-address { position: absolute; left: 245px; top: 34px; color: var(--ink); font-size: 12px; line-height: 16px; text-transform: uppercase; white-space: nowrap; }
  .card-back .phone { position: absolute; left: 245px; top: 86px; color: var(--phone-red); font-size: 24px; }
  .email { position: absolute; left: 245px; top: 114px; color: var(--ink); font-size: 12px; font-weight: 700; white-space: nowrap; }
  .message { position: absolute; left: 24px; top: 160px; width: 248px; color: #fff; font-size: 10.2px; line-height: 12px; text-align: justify; text-transform: uppercase; }
  .message p { margin-bottom: 12px; }
  .message strong { color: var(--phone-blue); }
  .card-back .web-pill { left: 35px; top: 335px; width: 224px; height: 21px; font-size: 12.5px; }
  .card-back .cursor { left: 252px; top: 346px; }
</style>
</head>
<body>

<section class="card card-front" aria-label="Postcard front">
  <div class="front-photo" role="img" aria-label="Photograph of a row of townhouses under a blue sky"></div>
  <svg class="front-bands" width="596" height="460" viewBox="0 0 596 460">
    <defs>
      <linearGradient id="redBand" x1="0" y1="0" x2="1" y2="0">
        <stop offset="0" stop-color="#e0302a"/><stop offset="1" stop-color="#b81a15"/>
      </linearGradient>
    </defs>
    <polygon points="0,0 596,0 596,18 470,22 300,40 80,78 0,92" fill="url(#redBand)"/>
    <polygon points="40,0 58,0 110,70 96,72" fill="var(--red-dark)" opacity=".7"/>
    <polygon points="0,360 596,360 596,460 0,460" fill="var(--navy)"/>
    <polygon points="500,440 596,400 596,412 520,446" fill="var(--navy-deep)"/>
  </svg>
  <div class="web-pill">www.northgatemortgageco.com</div>
  <svg class="cursor" width="14" height="18" viewBox="0 0 14 18"><path d="M1 1 L1 15 L5 11 L8 17 L10 16 L7 10 L12 10 Z" fill="#fff" stroke="#222" stroke-width="1"/></svg>
  <div class="brand-name"><span class="brand-mark"></span>NORTHGATE MORTGAGE</div>
  <div class="portrait-frame"><div class="portrait" role="img" aria-label="Portrait photo of the company president"></div></div>
  <div class="agent-name">Daniel Archer<small>President</small></div>
  <div class="phone">
    <svg width="26" height="18" viewBox="0 0 26 18"><path d="M2 7 Q13 -1 24 7 L21 10 L18 7 L8 7 L5 10 Z" fill="#fff"/><rect x="7" y="9" width="12" height="8" rx="2" fill="#fff"/></svg>
    248-555-0147
  </div>
  <div class="welcome">WELCOMES</div>
  <div class="welcome-sub">ALL CLIENTS TO MY NEW COMPANY</div>
</section>

<section class="card card-back" aria-label="Postcard back">
  <svg class="back-shapes" width="596" height="460" viewBox="0 0 596 460">
    <polygon points="448,0 596,0 596,460 75,460 75,376 288,376 288,148 448,148" fill="var(--panel-grey)"/>
    <polygon points="0,148 288,148 288,376 75,376 75,460 0,460" fill="var(--navy)"/>
  </svg>
  <div class="brand-name"><span class="brand-mark"></span>NORTHGATE MORTGAGE</div>
  <div class="return-address">Northgate Mortgage Company, LLC<br>2400 W. Maple Ridge<br>Suite 310 Troy, MI 48084</div>
  <div class="phone">
    <svg width="26" height="18" viewBox="0 0 26 18"><path d="M2 7 Q13 -1 24 7 L21 10 L18 7 L8 7 L5 10 Z" fill="#111"/><rect x="7" y="9" width="12" height="8" rx="2" fill="#111"/></svg>
    248-555-0147
  </div>
  <div class="email">dan@northgatemortgageco.com</div>
  <div class="message">
    <p>I am a mortgage broker located in Michigan and recently opened my own company <strong>Northgate Mortgage Company, LLC</strong> after working for another for 7 years.</p>
    <p><strong>Northgate Mortgage Company, LLC</strong> is committed to providing you with the best service, pricing, and programs to meet your mortgage needs. We are equipped to handle your conventional and government purchase or refinance loan needs.</p>
    <p>To learn more about applying for a mortgage with Northgate Mortgage Company, LLC please visit us at</p>
  </div>
  <div class="web-pill">www.northgatemortgageco.com</div>
  <svg class="cursor" width="14" height="18" viewBox="0 0 14 18"><path d="M1 1 L1 15 L5 11 L8 17 L10 16 L7 10 L12 10 Z" fill="#fff" stroke="#222" stroke-width="1"/></svg>
</section>

</body>
</html>
```